Redesign company trifold brochure

We are rebranding our company in September and looking for a more professional design for our brochure.

What we do - providing interdisciplinary care for those supporting ill, elderly and special needs pets at home following the human hospice model of care - is very novel and our brochure is key in explaining it and our offerings.

We serve dogs and cats. Most of the animals are quite sick, elderly. I have many personal and stock photos we can use in the brochure. Please - no pictures of puppies and/or kittens.

The hard part is fitting the info and message into a clear and concise format.

It must be appealing both to pet owners and vets (who are our primary source of patients through referrals).

It should covey WARMTH, COMPASSION, PROFESSIONALISM, and EXPERTISE.

Please look at our website www.LarkvaleAnimalRest.com for more info

We have until now used maroon and copper for colors - to reflect the "sunset" of the pets life. BUT are now changing to Navy, Teal and White to reflect calm, trust and competence.

We will use the same logo recolored.

Existing brochure and new logo are attached.

PLEASE ask questions!!
Updates

We have a library of stock images you are welcome to use. All have been legally acquired and we have the right to use them. You DO NOT have to use them, just sending along in case you wish to. https://www.filecrate.example/sh/q7rmt2wzp40kdyh/BBR8Kxtz-Pqmn3vd7yHsLcWqe?dl=0

Our colors are NAVY, TEAL and WHITE. For your reference, the navy we use is 99/87/44/55 (CMYK) The Teal we use is 76/11/44/0 (CMYK) Thank you!

Designers -- pleaseuse pictures of older pets (no puppies or kittens). Below is a link to stock photos we own that would be appropriate for use in the brochure. https://www.filecrate.example/sh/k416f8m2twr5zqa/BBQe3LmxtvRVZWPgb8JTFYs_4m?dl=0 THANK YOU!

Designers -- I would VERY much like to include a photo of a pet in a wheel chair. I have personal photos as well as (purchased) stock photos for this purpose which can be found at http://lnkr.example/LARWC-Pets-in-Wheelchairs Thank you!!

Today is the last day! Many of you have submitted beautiful designs and others are rolling in. I am so appreciative of your time and energy!! Please do not let the deadline pass without YOUR very BEST entry being submitted!! Thank you! - Miriam & All of us at Larkvale Animal Rest & Comfort Care

Target Market(s)

Pet Owners and Veterinarians

Industry/Entity Type

Pet Care

Font styles to use
Serif

Colors
0455a3
33b8a4
ffffff

Requirements
Must have
• Our logo and information about our services. Pictures of pets. Our contact info. PLEASE NOTE: this is a 2 sided brochure. Please submit both inside and outside.
Should not have
• puppies, kittens - anything off message

```html
<!DOCTYPE html>
<html lang="en">
<head>
<meta charset="utf-8">
<title>Larkvale Animal Rest &amp; Comfort Care – Trifold Brochure</title>
<link rel="stylesheet" href="https://fonts.googleapis.com/css2?family=Lato:ital,wght@0,400;0,700;0,900;1,700;1,900&family=Libre+Baskerville:wght@400;700&family=Oswald:wght@500&display=swap">
<style>
:root{
  --navy:#0f2148;
  --navy-deep:#0a1733;
  --teal:#17a79d;
  --teal-light:#2fbdb1;
  --white:#ffffff;
  --ink:#33414f;
  --page:#e9ecee;
}
*{box-sizing:border-box;margin:0;padding:0}
html,body{width:783px;height:1200px;overflow:hidden;background:var(--page)}
body{font-family:"Lato",sans-serif;color:var(--ink);position:relative}
.sheet{position:absolute;left:40px;width:703px;height:556px;background:var(--white);overflow:hidden;box-shadow:0 2px 8px rgba(0,0,0,.18)}
.sheet--outside{top:30px}
.sheet--inside{top:614px}
.panel{position:absolute;top:0;width:234.33px;height:556px;overflow:hidden}
.panel--1{left:0}.panel--2{left:234.33px}.panel--3{left:468.66px}
.abs{position:absolute}
.photo{position:absolute}
ul{list-style:none}

/* ---------- outside: beliefs ---------- */
.beliefs{background:linear-gradient(180deg,var(--navy-deep),var(--navy) 60%)}
.beliefs__title{position:absolute;left:16px;top:20px;color:var(--teal-light);font-weight:900;font-size:14px;letter-spacing:.4px}
.beliefs__list{position:absolute;left:16px;top:48px;width:205px;color:var(--white);font-size:9px;line-height:1.32}
.beliefs__list li{position:relative;padding-left:11px;margin-bottom:6px}
.beliefs__list li::before{content:"";position:absolute;left:0;top:3px;width:5px;height:5px;border-radius:50%;background:var(--teal-light)}

/* ---------- logo lockup ---------- */
.logo{position:absolute;display:flex;align-items:center;gap:8px}
.logo__mark{width:30px;height:30px;border-radius:50%;background:var(--teal);flex:none}
.logo__name{font-family:"Libre Baskerville",serif;font-size:14px;line-height:1.15;color:var(--navy)}
.logo--light .logo__name{color:var(--white)}

/* ---------- contact ---------- */
.contact{position:absolute;left:24px;top:428px;font-size:9.5px;font-weight:700;color:var(--navy);line-height:1.3}
.contact li{display:flex;gap:7px;margin-bottom:6px;align-items:flex-start}
.contact svg{flex:none;margin-top:1px}
.web-pill{position:absolute;left:18px;width:200px;height:36px;background:var(--navy);border-radius:12px 12px 0 0;color:var(--white);font-weight:900;font-size:11.5px;display:flex;align-items:center;justify-content:center}

/* ---------- cover ---------- */
.cover{background:var(--navy)}
.cover__banner{position:absolute;left:10px;right:0;bottom:0;height:84px;background:var(--teal);border-radius:18px 0 0 0;text-align:center;padding-top:12px}
.cover__line1{font-family:"Libre Baskerville",serif;font-weight:700;font-size:8.6px;color:var(--navy)}
.cover__line2{font-family:"Libre Baskerville",serif;font-weight:700;font-size:10.5px;color:var(--navy);margin-top:3px}
.cover__line3{font-family:"Oswald",sans-serif;font-size:13px;color:var(--white);margin-top:4px;letter-spacing:.3px}

/* ---------- inside: palliative ---------- */
.heading-navy{color:var(--navy);font-weight:900;text-align:center;font-size:13px;line-height:1.2}
.body-copy{font-size:8.6px;line-height:1.38;color:var(--ink)}
.lead{color:var(--teal);font-weight:900}
.sub-heading{color:var(--navy);font-weight:900;font-style:italic;font-size:10.5px}
.paw-list li{position:relative;padding-left:13px;margin-bottom:4px}
.paw-list li::before{content:"";position:absolute;left:1px;top:2.5px;width:6px;height:6px;border-radius:50%;background:var(--teal)}
.paw-list--white li::before{background:var(--white)}

/* ---------- services ---------- */
.services__title{position:absolute;left:16px;top:222px;color:var(--navy);font-weight:900;font-size:13.5px}
.services__intro{position:absolute;left:16px;top:243px;width:205px}
.services__intro p{margin-bottom:6px}
.services__list{position:absolute;left:16px;top:352px;width:210px;font-size:8.6px;line-height:1.3;color:var(--ink)}

/* ---------- team ---------- */
.team{background:linear-gradient(180deg,#139c93,var(--teal) 50%,#1ab0a5)}
.team__lead-in{position:absolute;left:14px;top:18px;width:205px;color:var(--navy);font-weight:900;font-style:italic;font-size:9.6px;line-height:1.25}
.team__cols{position:absolute;left:14px;top:50px;width:210px;display:flex;gap:8px;color:var(--white);font-size:8.6px;line-height:1.25}
.team__cols ul{flex:1}
.team__title{position:absolute;left:0;right:0;top:196px;text-align:center;color:var(--navy);font-weight:900;font-size:13.5px}
.team__lead{position:absolute;left:14px;top:222px;width:205px;color:var(--navy);font-weight:900;font-style:italic;font-size:9.2px;line-height:1.3}
.team__list{position:absolute;left:14px;top:252px;width:210px;color:var(--white);font-size:8.8px;line-height:1.25}

/* ---------- badge ---------- */
.badge{position:absolute;left:304px;top:8px;width:138px;height:138px;border-radius:50%;background:var(--navy);border:4px solid var(--white);text-align:center;color:var(--white);padding-top:28px}
.badge__small{font-size:9px;font-weight:900}
.badge__big{font-size:17px;font-weight:900;line-height:1.05;margin-top:4px}
.badge__teal{font-size:20px;font-weight:900;font-style:italic;color:var(--teal-light);line-height:1}
</style>
</head>
<body>

<!-- ================= OUTSIDE ================= -->
<section class="sheet sheet--outside" aria-label="Brochure outside">

  <article class="panel panel--1 beliefs">
    <h2 class="beliefs__title">WE BELIEVE</h2>
    <ul class="beliefs__list">
      <li>That animals are conscious beings, capable of thought, feeling, emotion and choice</li>
      <li>That each animal is an individual with his or her unique needs and wishes</li>
      <li>That all pets deserve to be pain-free</li>
      <li>That the principles of human hospice and palliative care are equally powerful when applied to animals</li>
      <li>That an interdisciplinary team is essential to addressing the needs of pets and their families through aging and illness</li>
      <li>That quality of life is subjective, best evaluated by the family who knows and loves the animal</li>
      <li>That there isn't one answer that is right for every animal or every family</li>
    </ul>
    <svg class="abs" style="left:0;top:300px" width="235" height="256" viewBox="0 0 235 256" aria-hidden="true">
      <path d="M0 150 C60 120 160 40 235 0 L235 256 L0 256 Z" fill="#17a79d"/>
      <path d="M0 190 C70 160 170 80 235 40 L235 256 L0 256 Z" fill="#ffffff"/>
    </svg>
    <div class="photo" role="img" aria-label="Photo of a senior terrier sitting upright, white with tan head"
         style="left:38px;top:300px;width:150px;height:256px;border-radius:70px 70px 0 0;background:radial-gradient(ellipse at 50% 40%,#f3efe8,#d9c7ad 60%,#b89a72)"></div>
  </article>

  <article class="panel panel--2">
    <svg class="abs" style="left:0;top:0" width="235" height="260" viewBox="0 0 235 260" aria-hidden="true">
      <path d="M0 0 L235 0 L235 60 C160 40 80 120 0 180 Z" fill="#17a79d"/>
      <path d="M0 0 L70 0 C40 60 20 110 0 140 Z" fill="#ffffff" opacity=".25"/>
    </svg>
    <div class="photo" role="img" aria-label="Photo of an older dog walking in a pet wheelchair on a beach"
         style="left:55px;top:62px;width:130px;height:130px;border-radius:50%;border:5px solid #ffffff;box-shadow:0 0 0 2px #17a79d;background:linear-gradient(180deg,#cfe1ec,#e5d8c2 60%,#bca985)"></div>
    <div class="photo" role="img" aria-label="Photo of a tabby cat resting on a rug"
         style="left:0;top:258px;width:234.33px;height:80px;background:linear-gradient(90deg,#8c8272,#b8ab95 45%,#d9cdb8)"></div>
    <div class="logo" style="left:28px;top:355px">
      <span class="logo__mark"></span>
      <span class="logo__name">Larkvale Animal Rest<br>&amp; Comfort Care</span>
    </div>
    <ul class="contact">
      <li><svg width="10" height="10" viewBox="0 0 24 24"><path fill="#17a79d" d="M6.6 10.8a15.1 15.1 0 006.6 6.6l2.2-2.2a1 1 0 011-.25 11.4 11.4 0 003.6.57 1 1 0 011 1V20a1 1 0 01-1 1A17 17 0 013 4a1 1 0 011-1h3.5a1 1 0 011 1c0 1.25.2 2.45.57 3.57a1 1 0 01-.25 1z"/></svg>(555) 302-LARK</li>
      <li><svg width="10" height="10" viewBox="0 0 24 24"><path fill="#17a79d" d="M12 2a7 7 0 00-7 7c0 5.25 7 13 7 13s7-7.75 7-13a7 7 0 00-7-7zm0 9.5A2.5 2.5 0 1112 6.5a2.5 2.5 0 010 5z"/></svg><span>418 Meadowgate Road Suite 210<br>Ashbrook, MA 01999</span></li>
      <li><svg width="10" height="10" viewBox="0 0 24 24"><path fill="#17a79d" d="M2 5h20v14H2z M2 5l10 8 10-8" stroke="#fff" stroke-width="1.5"/></svg>info@LarkvaleAnimalRest.com</li>
    </ul>
    <div class="web-pill" style="top:520px">www.LarkvaleAnimalRest.com</div>
  </article>

  <article class="panel panel--3 cover">
    <div class="photo" role="img" aria-label="Photo of a golden retriever seen from behind, watching a sunset over the sea"
         style="left:0;top:0;width:234.33px;height:345px;background:linear-gradient(180deg,#3a3a52,#c7783a 45%,#f2b24a 60%,#6a4a33)"></div>
    <svg class="abs" style="left:0;top:250px" width="235" height="110" viewBox="0 0 235 110" aria-hidden="true">
      <path d="M0 40 C70 90 160 100 235 60 L235 110 L0 110 Z" fill="#17a79d"/>
      <path d="M0 55 C70 100 160 110 235 72 L235 110 L0 110 Z" fill="#0f2148"/>
    </svg>
    <div class="logo logo--light" style="left:30px;top:378px">
      <span class="logo__mark"></span>
      <span class="logo__name" style="font-size:15px">Larkvale Animal Rest<br>&amp; Comfort Care</span>
    </div>
    <div class="cover__banner">
      <p class="cover__line1">SKILLED HOME CARE FOR ILL ELDERLY</p>
      <p class="cover__line2">AND SPECIAL NEEDS ANIMALS</p>
      <p class="cover__line3">COMPASSIONATE SUPPORT FOR FAMILIES</p>
    </div>
  </article>
</section>

<!-- ================= INSIDE ================= -->
<section class="sheet sheet--inside" aria-label="Brochure inside">

  <div class="photo" role="img" aria-label="Photo of an elderly boxer lying on green grass"
       style="left:0;top:0;width:470px;height:225px;background:linear-gradient(180deg,#9fbf5a,#6f9a35 55%,#4e7a25)"></div>
  <svg class="abs" style="left:0;top:140px" width="470" height="90" viewBox="0 0 470 90" aria-hidden="true">
    <path d="M0 58 C120 76 300 62 470 6 L470 90 L0 90 Z" fill="#0f2148"/>
    <path d="M0 70 C120 86 300 74 470 18 L470 90 L0 90 Z" fill="#ffffff"/>
  </svg>

  <article class="panel panel--1">
    <h2 class="heading-navy abs" style="left:0;right:0;top:244px">PALLIATIVE CARE<br>AND HOSPICE</h2>
    <div class="body-copy abs" style="left:16px;top:285px;width:205px">
      <p style="margin-bottom:7px"><span class="lead">PALLIATIVE CARE</span> seeks to relieve suffering and improve quality of life at all stages of illness, injury and disease, whether curable or not.</p>
      <p style="margin-bottom:9px"><span class="lead">HOSPICE</span> a special kind of Palliative Care focused on those with a life expectancy of less than one year.</p>
      <h3 class="sub-heading" style="margin-bottom:6px">BOTH PALLIATIVE CARE AND HOSPICE</h3>
      <ul class="paw-list">
        <li>Focus on living fully</li>
        <li>Recognize and address all suffering – physical, emotional, social and spiritual</li>
        <li>Use a team approach to meet the needs of the animal and his or her family</li>
        <li>Affirm life while viewing death as a natural, normal process</li>
      </ul>
    </div>
    <div class="web-pill" style="top:520px">www.LarkvaleAnimalRest.com</div>
  </article>

  <article class="panel panel--2">
    <h2 class="services__title">OUR SERVICES</h2>
    <div class="services__intro body-copy">
      <p>At Larkvale Animal Rest &amp; Comfort Care, our only goal is to support you in providing the very best care for your beloved companion in your own home.</p>
      <p>We work as a team to address the needs of your entire family. We come with no agenda and no prescribed plan, but rather follow your needs and wishes as they evolve and change over time. Some of the services we offer are:</p>
    </div>
    <ul class="services__list paw-list">
      <li>Visiting and support</li>
      <li>Administration of medication &amp; fluids</li>
      <li>Overnight and respite care</li>
      <li>Check-ins, exercise and play</li>
      <li>Assistance evaluating pain, quality of life, and end of life choices</li>
      <li>Coordination of care with your vet and other care professionals</li>
      <li>Home cooked meals and treats</li>
      <li>Transportation and errand running</li>
      <li>Equipment and supplies</li>
      <li>Funerals and memorials</li>
      <li>Bereavement support</li>
    </ul>
  </article>

  <div class="badge">
    <p class="badge__small">WE ARE HERE</p>
    <p class="badge__big">FOR YOU</p>
    <p class="badge__teal">24 HOURS</p>
    <p class="badge__big" style="font-size:15px">A DAY</p>
  </div>
  <svg class="abs" style="left:290px;top:-6px" width="180" height="180" viewBox="0 0 180 180" aria-hidden="true">
    <defs><path id="badge-arc" d="M30 150 A80 80 0 0 0 150 20"/></defs>
    <text font-family="Lato, sans-serif" font-weight="900" font-style="italic" font-size="13" letter-spacing="1">
      <textPath href="#badge-arc" startOffset="2%"><tspan fill="#17a79d">EVERY DAY</tspan><tspan fill="#0f2148"> OF THE YEAR</tspan></textPath>
    </text>
  </svg>

  <article class="panel panel--3 team">
    <p class="team__lead-in">OUR SKILLED TEAM MEMBERS CAN ALSO PROVIDE:</p>
    <div class="team__cols">
      <ul class="paw-list paw-list--white">
        <li>Massage and Touch Work</li>
        <li>Cold LASER Treatments</li>
        <li>Reiki</li>
        <li>Passive Range of Motion (PROM)</li>
        <li>Rehabilitation Support</li>
      </ul>
      <ul class="paw-list paw-list--white">
        <li>Grooming</li>
        <li>Essential Oils</li>
        <li>Flower Essences</li>
        <li>Aroma Therapy</li>
        <li>Music Therapy</li>
        <li>Pet Therapy</li>
      </ul>
    </div>
    <h2 class="team__title">OUR TEAM</h2>
    <p class="team__lead">LEAD BY MIRIAM COLDWELL, C.T. OUR INTERDISCIPLINARY TEAM INCLUDES:</p>
    <ul class="team__list paw-list paw-list--white">
      <li>Certified Thanatologist</li>
      <li>Certified Veterinary Technicians</li>
      <li>Interfaith Spiritual Advisor</li>
      <li>Certified Small Animal Massage Therapist</li>
      <li>Animal Care Specialists</li>
      <li>Hospice Assistants</li>
      <li>Client Care Coordinator</li>
    </ul>
    <svg class="abs" style="left:0;top:380px" width="235" height="176" viewBox="0 0 235 176" aria-hidden="true">
      <path d="M0 60 C60 20 150 0 235 10 L235 176 L0 176 Z" fill="#ffffff"/>
      <path d="M0 150 C80 120 170 130 235 150 L235 176 L0 176 Z" fill="#0f2148"/>
    </svg>
    <div class="photo" role="img" aria-label="Photo of a senior grey and white cat lying down"
         style="left:60px;top:410px;width:170px;height:120px;border-radius:60px 60px 20px 20px;background:radial-gradient(ellipse at 45% 45%,#f4f4f2,#cfcac2 55%,#a39a8c)"></div>
  </article>
</section>

</body>
</html>
```